Health and wellnes company needs business cards

We are a Health and wellness business just relocated to Spain. Here nobody knows our business so we would like to put some of our services on the card. Clean design with logo.

Contact Information for Business Card

Brightmeadow
Clara & Tobias Wennberg
Calle de los Almendros 17
Villaclara del Mar
Mobile: 0046 731 402768
info@brightmeadow-example.se

Font styles to use
Serif

Colors
85cae6
85acd3
b768aa

Requirements
Must have
• these Services somewhere on the card
• - Private or group yoga
• - Energy healing
• - Kitesurfing lessons
• - Massage
• LOgo somewhere
Nice to have
• Colours that go with the logo please

```html
<!DOCTYPE html>
<html lang="en">
<head>
<meta charset="utf-8">
<title>Brightmeadow – Business Cards</title>
<link rel="stylesheet" href="https://fonts.googleapis.com/css2?family=PT+Serif:ital,wght@0,400;0,700;1,700&display=swap">
<style>
  :root {
    --canvas: #d9d6d1;
    --card: #121212;
    --teal: #5cc3cc;
    --teal-light: #85cae6;
    --navy: #1f3f78;
    --ink-light: #f2f2f2;
  }
  * { box-sizing: border-box; margin: 0; padding: 0; }
  html, body {
    width: 1200px; height: 900px; overflow: hidden;
    background: var(--canvas);
    font-family: "PT Serif", Georgia, serif;
  }
  .sheet {
    width: 1200px; height: 900px;
    display: flex; flex-direction: column; align-items: center; justify-content: center;
    gap: 40px;
  }
  .card {
    width: 720px; height: 400px;
    background: var(--card);
    border-radius: 4px;
    box-shadow: 0 10px 24px rgba(0,0,0,.28);
    position: relative;
    color: var(--ink-light);
  }
  /* Front */
  .card-front {
    display: flex; flex-direction: column; align-items: center;
    padding-top: 52px;
  }
  .services-title {
    font-style: italic; font-weight: 700; color: var(--teal);
    font-size: 26px; letter-spacing: .5px;
  }
  .services-list {
    color: var(--teal); font-size: 27px; text-align: center; line-height: 1.22;
    margin-top: 2px; letter-spacing: .4px;
  }
  .brand {
    display: flex; align-items: center; gap: 16px;
    margin-top: 70px;
    white-space: nowrap;
  }
  .brand-mark {
    width: 46px; height: 46px; border-radius: 50%;
    border: 4px solid var(--teal-light); flex: none;
  }
  .brand-name {
    font-size: 44px; font-weight: 400; letter-spacing: 3px;
    color: var(--teal-light); text-transform: uppercase;
  }
  /* Back */
  .card-back .brand {
    position: absolute; left: 44px; top: 205px; margin: 0; gap: 10px;
  }
  .card-back .brand-mark { width: 34px; height: 34px; border-width: 4px; border-color: var(--teal); }
  .card-back .brand-name { font-size: 27px; color: var(--navy); letter-spacing: 1.5px; }
  .contact {
    position: absolute; left: 378px; top: 66px; width: 310px;
    white-space: nowrap;
  }
  .contact-names {
    font-weight: 700; color: var(--teal); font-size: 22px; margin-bottom: 12px;
  }
  .contact-company {
    font-weight: 700; color: var(--teal); font-size: 17px;
  }
  .contact-address { font-size: 17px; line-height: 1.3; font-style: normal; }
  .contact-lines { list-style: none; margin-top: 8px; font-size: 17px; line-height: 1.5; }
  .contact-lines li { display: flex; align-items: center; gap: 9px; }
  .contact-lines svg { width: 13px; height: 13px; flex: none; }
</style>
</head>
<body>
<main class="sheet">
  <section class="card card-front">
    <h2 class="services-title">Our Services:</h2>
    <p class="services-list">Private or group yoga | Energy healing<br>Kitesurfing lessons | Massage</p>
    <div class="brand">
      <span class="brand-mark"></span>
      <span class="brand-name">Brightmeadow</span>
    </div>
  </section>

  <section class="card card-back">
    <div class="brand">
      <span class="brand-mark"></span>
      <span class="brand-name">Brightmeadow</span>
    </div>
    <div class="contact">
      <p class="contact-names">Clara &amp; Tobias Wennberg</p>
      <p class="contact-company">Brightmeadow</p>
      <address class="contact-address">Calle de los Almendros 17<br>Villaclara del Mar</address>
      <ul class="contact-lines">
        <li>
          <svg viewBox="0 0 16 16" aria-hidden="true"><path fill="#85cae6" d="M3.6 1.5l2.3 2.6-1.3 1.7c.9 2 2.5 3.6 4.6 4.6l1.7-1.3 2.6 2.3-1.4 2.1C7 13.3 2.7 9 1.5 3z"/></svg>
          <span>0046 731 402768</span>
        </li>
        <li>
          <svg viewBox="0 0 16 16" aria-hidden="true"><rect x="1" y="3" width="14" height="10" fill="#85cae6"/><path d="M1 3l7 6 7-6" fill="none" stroke="#121212" stroke-width="1.3"/></svg>
          <span>info@brightmeadow-example.se</span>
        </li>
        <li>
          <svg viewBox="0 0 16 16" aria-hidden="true"><circle cx="8" cy="8" r="6.5" fill="none" stroke="#85cae6" stroke-width="1.6"/><path d="M1.5 8h13M8 1.5c-3 3.5-3 9.5 0 13M8 1.5c3 3.5 3 9.5 0 13" fill="none" stroke="#85cae6" stroke-width="1.2"/></svg>
          <span>www.brightmeadow-example.se</span>
        </li>
      </ul>
    </div>
  </section>
</main>
</body>
</html>
```